Newspaper advert design

Chinese Horoscopes : Needed the 12 animals one for males, one for females. Listed against the name and picture of animal, the telephone number of a premium rate telephone line.. So in total 24 phone numbers.

Two columns for a half a page newspaper/magazine advertisement. 12 zodiac signs for females - 12 zodiac signs for males.

Eye catching colors needed. Bright colors.

The Chinese animals symbols to look as "cartoon-ish as possible) Bold rounded fonts.

Chinese Horoscopes :  Needed the 12 animals one for males, one for females.  Listed against the name and picture of animal, the telephone number of a premium rate telephone line..  So in total 24 phone numbers.

Two columns for a half a page newspaper/magazine advertisement.  12 zodiac signs for females - 12 zodiac signs for males.

The Chinese animals symbols to look as "cartoon-ish as possible)  Bold rounded fonts.

Must have the slogan "Find your inner animal" underneath the list.

Women age rage 18 to 60.

• Bright colors.
Bold fonts.

The heading Chinese Horoscopes

"Find your inner animal" at the bottom of the advertisement.

```html
<!DOCTYPE html>
<html lang="en">
<head>
<meta charset="utf-8">
<title>Chinese Horoscope – Find your inner animal</title>
<link rel="stylesheet" href="https://fonts.googleapis.com/css2?family=Cinzel:wght@700;900&family=Lilita+One&family=Nunito:wght@700;800;900&display=swap">
<style>
  :root {
    --page-bg: #e8e3da;
    --plum: #9b3a5c;
    --rose: #c66a6a;
    --amber: #efb248;
    --sun: #f3d467;
    --sage: #8db3a2;
    --teal: #2e8a94;
    --deep-teal: #1b6a7a;
    --gold: #e7b73c;
    --gold-dark: #8a5a12;
    --navy: #1d2b4f;
    --maroon-box: #4a0f24;
    --berry-box: #8a2456;
    --teal-box: #0f4655;
    --aqua-box: #3b8f9c;
    --cream: #fff3d6;
    --footer-yellow: #f5c400;
    --footer-brown: #5a3a28;
  }
  * { box-sizing: border-box; margin: 0; padding: 0; }
  html, body { width: 1200px; height: 960px; overflow: hidden; background: var(--page-bg); }
  body { position: relative; font-family: "Nunito", sans-serif; }

  .advert {
    position: absolute; left: 292px; top: 20px; width: 616px; height: 920px;
    overflow: hidden;
    background: linear-gradient(90deg, var(--plum) 0%, var(--rose) 24%, var(--amber) 42%, var(--sun) 50%, var(--sage) 62%, var(--teal) 80%, var(--deep-teal) 100%);
    box-shadow: 0 6px 18px rgba(0,0,0,.25);
  }
  .advert::before {
    content: ""; position: absolute; inset: 0;
    background: linear-gradient(180deg, rgba(0,0,0,.08) 0%, rgba(0,0,0,0) 30%, rgba(0,0,0,0) 80%, rgba(0,0,0,.12) 100%);
  }

  .dragon {
    position: absolute; top: 14px; width: 76px; height: 66px; border-radius: 8px;
    background: linear-gradient(140deg, #d8ab4c 0%, #a77a2a 55%, #6f4d17 100%);
    border: 1px solid rgba(255,230,160,.55);
    box-shadow: inset 0 0 0 3px rgba(0,0,0,.12), 0 2px 4px rgba(0,0,0,.3);
    opacity: .9;
  }
  .dragon--left { left: 14px; }
  .dragon--right { right: 14px; }

  .title {
    position: absolute; top: 16px; left: 0; width: 100%; text-align: center;
    font-family: "Lilita One", sans-serif; font-size: 36px; letter-spacing: 1px;
    color: var(--gold); text-shadow: 0 2px 0 var(--gold-dark), 0 3px 4px rgba(0,0,0,.45);
  }
  .tagline {
    position: absolute; top: 60px; left: 104px; width: 408px; text-align: center;
    font-weight: 900; font-size: 12px; line-height: 1.3; color: var(--navy);
  }

  .half { position: absolute; top: 0; width: 308px; height: 100%; }
  .half--female { left: 0; }
  .half--male { left: 308px; }

  .group-title {
    position: absolute; top: 104px; left: 62px; width: 184px; height: 34px; border-radius: 6px;
    display: flex; align-items: center; justify-content: center; gap: 10px;
    font-family: "Cinzel", serif; font-weight: 900; font-size: 22px; color: var(--cream);
    box-shadow: 0 2px 4px rgba(0,0,0,.35);
  }
  .group-title::before, .group-title::after {
    content: ""; width: 18px; height: 2px; background: var(--gold);
  }
  .half--female .group-title { background: var(--maroon-box); }
  .half--male .group-title { background: var(--teal-box); }

  .signs {
    position: absolute; top: 150px; left: 0; width: 308px;
    display: grid; grid-template-columns: repeat(2, 128px); justify-content: center;
    column-gap: 14px; row-gap: 6px;
  }
  .sign { height: 111px; display: flex; flex-direction: column; align-items: center; }
  .sign-name {
    font-family: "Cinzel", serif; font-weight: 900; font-size: 13px; line-height: 16px;
    color: var(--cream); text-shadow: 0 1px 2px rgba(0,0,0,.7);
  }
  .sign-art {
    width: 76px; height: 56px; border: 2px solid #fff; border-radius: 4px;
    box-shadow: 0 1px 3px rgba(0,0,0,.3);
  }
  .sign-rate {
    margin-top: 3px; width: 128px; height: 34px; border-radius: 6px; padding: 0 6px;
    border: 1px dashed rgba(255,255,255,.55);
    display: flex; flex-direction: column; justify-content: center; align-items: center;
    font-size: 8.5px; font-weight: 800; line-height: 1.3; color: var(--cream);
    white-space: nowrap;
  }
  .half--female .sign:nth-child(4n+1) .sign-rate,
  .half--female .sign:nth-child(4n+4) .sign-rate { background: var(--maroon-box); }
  .half--female .sign:nth-child(4n+2) .sign-rate,
  .half--female .sign:nth-child(4n+3) .sign-rate { background: var(--berry-box); }
  .half--male .sign:nth-child(4n+1) .sign-rate,
  .half--male .sign:nth-child(4n+4) .sign-rate { background: var(--teal-box); }
  .half--male .sign:nth-child(4n+2) .sign-rate,
  .half--male .sign:nth-child(4n+3) .sign-rate { background: var(--aqua-box); }

  .art-rat { background: linear-gradient(135deg, #d9e4f7, #b6c6e8); }
  .art-ox { background: linear-gradient(135deg, #f3d9a8, #d99a55); }
  .art-tiger { background: linear-gradient(135deg, #f7d7a0, #d98a3a); }
  .art-rabbit { background: linear-gradient(135deg, #e3eefa, #b8d2ef); }
  .art-dragon { background: linear-gradient(135deg, #d7f0f3, #9fd1dc); }
  .art-snake { background: linear-gradient(135deg, #ebe0f6, #c2aee3); }
  .art-horse { background: linear-gradient(135deg, #efd3b0, #b07a45); }
  .art-goat { background: linear-gradient(135deg, #fbe8ef, #f2c2d3); }
  .art-monkey { background: linear-gradient(135deg, #f4dcc0, #c98a52); }
  .art-rooster { background: linear-gradient(135deg, #fdf1c8, #f3b7a8); }
  .art-dog { background: linear-gradient(135deg, #f7ecd9, #d8b88c); }
  .art-pig { background: linear-gradient(135deg, #fde6ef, #f5bcd2); }

  .footer {
    position: absolute; left: 0; bottom: 0; width: 100%; height: 66px;
    background: linear-gradient(180deg, rgba(90,58,40,0) 0%, rgba(90,58,40,.75) 45%, var(--footer-brown) 100%);
  }
  .slogan {
    position: absolute; left: 30px; bottom: 16px;
    font-family: "Cinzel", serif; font-weight: 900; font-size: 22px; color: #fff;
    text-shadow: 0 2px 3px rgba(0,0,0,.5);
  }
  .footer-bar { position: absolute; left: 0; bottom: 0; width: 100%; height: 10px; background: var(--footer-yellow); }
</style>
</head>
<body>
<main class="advert">
  <div class="dragon dragon--left" role="img" aria-label="Golden Chinese dragon ornament"></div>
  <div class="dragon dragon--right" role="img" aria-label="Golden Chinese dragon ornament"></div>
  <h1 class="title">Chinese Horoscope</h1>
  <p class="tagline">Discover the animal within for him or her, personality, career, love, relationship compatibility and much, much more...</p>

  <section class="half half--female">
    <h2 class="group-title">Female</h2>
    <div class="signs">
      <div class="sign"><span class="sign-name">Rat</span><div class="sign-art art-rat" role="img" aria-label="Cartoon rat costume character"></div><div class="sign-rate"><span>Premium Rate : 50¥</span><span>Telephone: 123-456-7890</span></div></div>
      <div class="sign"><span class="sign-name">Ox</span><div class="sign-art art-ox" role="img" aria-label="Cartoon ox costume character"></div><div class="sign-rate"><span>Premium Rate : 50¥</span><span>Telephone: 123-456-7890</span></div></div>
      <div class="sign"><span class="sign-name">Tiger</span><div class="sign-art art-tiger" role="img" aria-label="Cartoon tiger costume character"></div><div class="sign-rate"><span>Premium Rate : 50¥</span><span>Telephone: 123-456-7890</span></div></div>
      <div class="sign"><span class="sign-name">Rabbit</span><div class="sign-art art-rabbit" role="img" aria-label="Cartoon rabbit costume character"></div><div class="sign-rate"><span>Premium Rate : 50¥</span><span>Telephone: 123-456-7890</span></div></div>
      <div class="sign"><span class="sign-name">Dragon</span><div class="sign-art art-dragon" role="img" aria-label="Cartoon dragon costume character"></div><div class="sign-rate"><span>Premium Rate : 50¥</span><span>Telephone: 123-456-7890</span></div></div>
      <div class="sign"><span class="sign-name">Snake</span><div class="sign-art art-snake" role="img" aria-label="Cartoon snake costume character"></div><div class="sign-rate"><span>Premium Rate : 50¥</span><span>Telephone: 123-456-7890</span></div></div>
      <div class="sign"><span class="sign-name">Horse</span><div class="sign-art art-horse" role="img" aria-label="Cartoon horse costume character"></div><div class="sign-rate"><span>Premium Rate : 50¥</span><span>Telephone: 123-456-7890</span></div></div>
      <div class="sign"><span class="sign-name">Goat</span><div class="sign-art art-goat" role="img" aria-label="Cartoon goat costume character"></div><div class="sign-rate"><span>Premium Rate : 50¥</span><span>Telephone: 123-456-7890</span></div></div>
      <div class="sign"><span class="sign-name">Monkey</span><div class="sign-art art-monkey" role="img" aria-label="Cartoon monkey costume character"></div><div class="sign-rate"><span>Premium Rate : 50¥</span><span>Telephone: 123-456-7890</span></div></div>
      <div class="sign"><span class="sign-name">Rooster</span><div class="sign-art art-rooster" role="img" aria-label="Cartoon rooster costume character"></div><div class="sign-rate"><span>Premium Rate : 50¥</span><span>Telephone: 123-456-7890</span></div></div>
      <div class="sign"><span class="sign-name">Dog</span><div class="sign-art art-dog" role="img" aria-label="Cartoon dog costume character"></div><div class="sign-rate"><span>Premium Rate : 50¥</span><span>Telephone: 123-456-7890</span></div></div>
      <div class="sign"><span class="sign-name">Pig</span><div class="sign-art art-pig" role="img" aria-label="Cartoon pig costume character"></div><div class="sign-rate"><span>Premium Rate : 50¥</span><span>Telephone: 123-456-7890</span></div></div>
    </div>
  </section>

  <section class="half half--male">
    <h2 class="group-title">Male</h2>
    <div class="signs">
      <div class="sign"><span class="sign-name">Rat</span><div class="sign-art art-rat" role="img" aria-label="Cartoon rat costume character"></div><div class="sign-rate"><span>Premium Rate : 55¥</span><span>Telephone: 123-456-7890</span></div></div>
      <div class="sign"><span class="sign-name">Ox</span><div class="sign-art art-ox" role="img" aria-label="Cartoon ox costume character"></div><div class="sign-rate"><span>Premium Rate : 55¥</span><span>Telephone: 123-456-7890</span></div></div>
      <div class="sign"><span class="sign-name">Tiger</span><div class="sign-art art-tiger" role="img" aria-label="Cartoon tiger costume character"></div><div class="sign-rate"><span>Premium Rate : 55¥</span><span>Telephone: 123-456-7890</span></div></div>
      <div class="sign"><span class="sign-name">Rabbit</span><div class="sign-art art-rabbit" role="img" aria-label="Cartoon rabbit costume character"></div><div class="sign-rate"><span>Premium Rate : 55¥</span><span>Telephone: 123-456-7890</span></div></div>
      <div class="sign"><span class="sign-name">Dragon</span><div class="sign-art art-dragon" role="img" aria-label="Cartoon dragon costume character"></div><div class="sign-rate"><span>Premium Rate : 55¥</span><span>Telephone: 123-456-7890</span></div></div>
      <div class="sign"><span class="sign-name">Snake</span><div class="sign-art art-snake" role="img" aria-label="Cartoon snake costume character"></div><div class="sign-rate"><span>Premium Rate : 55¥</span><span>Telephone: 123-456-7890</span></div></div>
      <div class="sign"><span class="sign-name">Horse</span><div class="sign-art art-horse" role="img" aria-label="Cartoon horse costume character"></div><div class="sign-rate"><span>Premium Rate : 55¥</span><span>Telephone: 123-456-7890</span></div></div>
      <div class="sign"><span class="sign-name">Goat</span><div class="sign-art art-goat" role="img" aria-label="Cartoon goat costume character"></div><div class="sign-rate"><span>Premium Rate : 55¥</span><span>Telephone: 123-456-7890</span></div></div>
      <div class="sign"><span class="sign-name">Monkey</span><div class="sign-art art-monkey" role="img" aria-label="Cartoon monkey costume character"></div><div class="sign-rate"><span>Premium Rate : 55¥</span><span>Telephone: 123-456-7890</span></div></div>
      <div class="sign"><span class="sign-name">Rooster</span><div class="sign-art art-rooster" role="img" aria-label="Cartoon rooster costume character"></div><div class="sign-rate"><span>Premium Rate : 55¥</span><span>Telephone: 123-456-7890</span></div></div>
      <div class="sign"><span class="sign-name">Dog</span><div class="sign-art art-dog" role="img" aria-label="Cartoon dog costume character"></div><div class="sign-rate"><span>Premium Rate : 55¥</span><span>Telephone: 123-456-7890</span></div></div>
      <div class="sign"><span class="sign-name">Pig</span><div class="sign-art art-pig" role="img" aria-label="Cartoon pig costume character"></div><div class="sign-rate"><span>Premium Rate : 55¥</span><span>Telephone: 123-456-7890</span></div></div>
    </div>
  </section>

  <footer class="footer">
    <p class="slogan">Find your inner animal</p>
    <div class="footer-bar"></div>
  </footer>
</main>
</body>
</html>
```